DOG DAYCARE BILLBOARD

Design a bold exciting billboard that can be read easily from a distance! Our goal is brand awareness and showcasing the services we offer (Boarding, Grooming, Daycare, and Training.
we would like to see examples with the phrase "your best friend's best day". Our name Bright Meadow Canine Activity Center (or just Bright Meadow might work better and could be bigger) and the services we provide.
(there are two examples of what we like included in the pictures)
you can find more information o our website at pawplayhouse@mailbox-example.com.

```html
<!DOCTYPE html>
<html lang="en">
<head>
<meta charset="utf-8">
<title>Bright Meadow Canine Activity Center — Billboard</title>
<link href="https://fonts.googleapis.com/css2?family=Montserrat:wght@700;900&family=Michroma&display=swap" rel="stylesheet">
<style>
  :root {
    --backdrop: #808080;
    --board: #ffffff;
    --ink: #000000;
    --olive: #b0a20c;
    --on-olive: #ffffff;
  }
  * { margin: 0; padding: 0; box-sizing: border-box; }
  html, body { width: 948px; height: 1200px; overflow: hidden; }
  body { background: var(--backdrop); position: relative; }

  .billboard {
    position: absolute;
    left: 44px; top: 434px;
    width: 860px; height: 332px;
    background: var(--board);
    overflow: hidden;
  }
  .service-band {
    position: absolute;
    left: 0; right: 0; top: 249px; bottom: 0;
    background: var(--olive);
  }
  .brand-mark {
    position: absolute;
    left: 78px; top: 28px;
    width: 150px; height: 150px;
    border-radius: 50%;
    background: var(--ink);
  }
  .brand-name {
    position: absolute;
    right: 40px; top: 30px;
    font-family: "Montserrat", sans-serif;
    font-weight: 900;
    font-size: 72px;
    line-height: 0.98;
    color: var(--ink);
    text-align: right;
    letter-spacing: -1px;
  }
  .rule {
    position: absolute;
    background: var(--ink);
  }
  .rule--main { left: 30px; width: 796px; top: 202px; height: 3px; }
  .rule--fine { left: 330px; width: 496px; top: 211px; height: 1px; }
  .descriptor {
    position: absolute;
    left: 26px; top: 229px;
    width: 800px; height: 38px;
    border-radius: 19px;
    background: var(--ink);
    color: var(--board);
    font-family: "Michroma", sans-serif;
    font-size: 20px;
    letter-spacing: 6px;
    display: flex; align-items: center; justify-content: center;
  }
  .services {
    position: absolute;
    left: 0; right: 0; top: 272px;
    display: flex; justify-content: center; align-items: center;
    gap: 16px;
    font-family: "Montserrat", sans-serif;
    font-weight: 700;
    font-size: 32px;
    color: var(--on-olive);
    list-style: none;
  }
  .services .divider {
    width: 3px; height: 32px; background: var(--on-olive);
  }
</style>
</head>
<body>
  <section class="billboard" aria-label="Bright Meadow Canine Activity Center billboard">
    <div class="service-band"></div>
    <div class="brand-mark" aria-hidden="true"></div>
    <h1 class="brand-name">Bright<br>Meadow</h1>
    <div class="rule rule--main" aria-hidden="true"></div>
    <div class="rule rule--fine" aria-hidden="true"></div>
    <p class="descriptor">CANINE ACTIVITY CENTER LLC</p>
    <ul class="services">
      <li>Boarding</li><li class="divider" aria-hidden="true"></li>
      <li>Grooming</li><li class="divider" aria-hidden="true"></li>
      <li>Daycare</li><li class="divider" aria-hidden="true"></li>
      <li>Training</li>
    </ul>
  </section>
</body>
</html>
```